Commercial/Corporate Law Firm needs Website Design

Hi guys. I've started up a new law firm and would love your help designing an attractive website. I'll need both design and coding, and to make it easy for us to edit as necessary later, I think it should be built off a Wordpress.org structure.
FIRST IMPRESSIONS
It's very important that the first impression of the website really captures our prospective clients' attention and impresses them. Their first three seconds needs to be good.
I imagine the homepage may be short, with a menu bar and a compelling image, and with a tagline overlaid or underneath (eg. "It's about results.")
The image should be related to our practice areas: eg. IPOs, corporate transactions, or commercial negotiations.
I have previously suggested there could be a skyline image of Sydney or Adelaide. However, because we are based in Adelaide, I don't think Sydney is appropriate - and Adelaide is probably too boring to use.
HOMEPAGE
Being a new firm, we don't have many existing testimonials, and I will be the only lawyer to start with. So we need to focus on the nature of the services we will provide and how my experience can help them. We have an existing logo to use, and I would like the website colour scheme not to clash with that logo (dark blue and white).
After the initial image and tagline there should be a brief introduction to each of the main areas of work, eg. "We specialise in three main areas of practice:"
1. Corporate Transactions and Regulation
2. Business Law and Dispute Resolution
3. Migration Assistance
These should each have an appropriate photo and link to a separate page that briefly describes our services in that area.
Below that there should be a message from me with a photo. Finally, at the bottom, there should be a "Contact Us" section which shows a Google image of our address, contact details, and then our logo with colours inverted.
OTHER PAGES
While we will need some other pages, they should all be fairly simple. I think we will need one page to say "About Us", where I will put information about my experience. I think we will then need one page for each of the 3 areas listed above, which just needs an appropriate image and then text to describe the service. Finally, a "Contact Us" page which I imagine will be the same as the bottom of the homepage.
OTHER DETAILS
For now you can use details from my LinkedIn page to fill out any other text as necessary, or the photo.
Because the logo is square, I would prefer the design of the website also to be rectangular.
Looking forward to seeing your work! Thank you.
Good luck,
Marcus
Target Market(s)
Potential clients:
Businesses with legal issues or disputes
Companies wishing to list on the stock market

```html
<!DOCTYPE html>
<html lang="en">
<head>
<meta charset="utf-8">
<title>Halvern Legal</title>
<link rel="stylesheet" href="https://fonts.googleapis.com/css2?family=Montserrat:wght@400;600;700;800&family=Roboto:wght@300;400;500;700&display=swap">
<style>
:root{
  --navy:#1d3560;
  --navy-deep:#16294b;
  --blue-light:#5fb0dc;
  --cyan:#3fb3e6;
  --ink:#1f3561;
  --grey:#9a9fa6;
  --grey-light:#c4c8cd;
  --map:#2f2f31;
  --white:#ffffff;
}
*{margin:0;padding:0;box-sizing:border-box}
html,body{width:1200px;height:3586px;overflow:hidden}
body{position:relative;background:var(--white);font-family:"Roboto",sans-serif;color:var(--ink)}
.abs{position:absolute}

/* header */
.hero{left:0;top:0;width:1200px;height:540px;
  clip-path:polygon(0 0,1200px 0,1200px 435px,320px 540px,0 455px);
  background:linear-gradient(180deg,#4e6a86 0%,#3d5a78 35%,#1d3a55 62%,#0f2438 100%)}
.hero-shade{left:0;top:0;width:1200px;height:540px;
  clip-path:polygon(0 0,1200px 0,1200px 435px,320px 540px,0 455px);
  background:linear-gradient(90deg,rgba(12,28,52,.55),rgba(12,28,52,.15))}
.navbar{left:0;top:0;width:1200px;height:82px;background:linear-gradient(90deg,#1b3560,#213f6e)}
.brand{left:248px;top:14px;width:80px;display:flex;flex-direction:column;align-items:center;gap:5px;color:var(--white);
  font-family:"Montserrat",sans-serif;font-weight:600;font-size:10px;line-height:11px;letter-spacing:2px;text-align:center}
.brand-mark{width:22px;height:22px;border:2px solid var(--white)}
.nav-link{top:34px;font-family:"Montserrat",sans-serif;font-size:10px;font-weight:600;color:var(--white);
  letter-spacing:.5px;line-height:12px;white-space:nowrap}
.nav-link.active{border-bottom:2px solid var(--white);padding-bottom:4px}
.nav-home{left:490px}
.nav-about{left:561px}
.nav-services{left:636px}
.nav-contact{left:724px}
.btn-start{left:828px;top:25px;width:112px;height:28px;border-radius:14px;background:var(--white);
  color:var(--navy);font-family:"Montserrat",sans-serif;font-size:9.5px;font-weight:700;white-space:nowrap;
  display:flex;align-items:center;justify-content:center}
.hero-eyebrow{left:256px;top:238px;color:var(--white);font-family:"Montserrat",sans-serif;font-size:13px;font-weight:600}
.hero-title{left:254px;top:254px;color:var(--white);font-family:"Montserrat",sans-serif;font-size:37px;font-weight:700;letter-spacing:.5px}
.hero-tag{left:256px;top:298px;color:var(--cyan);font-family:"Montserrat",sans-serif;font-size:19px;font-weight:700;letter-spacing:.5px}
.hero-text{left:256px;top:328px;width:460px;color:#d7dee7;font-size:10.5px;line-height:14px}
.btn-pill{height:26px;border-radius:13px;font-family:"Montserrat",sans-serif;font-size:9px;font-weight:600;
  color:var(--white);display:flex;align-items:center;justify-content:center;letter-spacing:.5px;white-space:nowrap}
.btn-learn{left:256px;top:395px;width:88px;background:var(--navy)}
.btn-contact{left:357px;top:395px;width:88px;border:1.5px solid var(--white)}

/* intro */
.eyebrow-s{font-size:10px;color:var(--grey)}
.intro-eyebrow{left:245px;top:726px}
.intro-title{left:244px;top:748px;font-family:"Montserrat",sans-serif;font-size:35px;font-weight:700;line-height:42px;color:var(--navy)}
.intro-rule{left:245px;top:845px;width:36px;height:2px;background:var(--navy)}
.photo{display:block}
.photo-handshake{left:503px;top:632px;width:194px;height:226px;background:linear-gradient(135deg,#e8e8e8,#8f8f8f 55%,#cfcfcf)}
.photo-signing{left:740px;top:712px;width:195px;height:225px;background:linear-gradient(160deg,#f2f2f2,#b9b9b9 50%,#5c5c5c)}
.small-text{font-size:10px;line-height:14px;color:var(--grey-light)}
.intro-text-a{left:503px;top:870px;width:194px}
.intro-text-b{left:740px;top:635px;width:195px}

.about-eyebrow{left:266px;top:1088px;font-size:9px;color:var(--grey);letter-spacing:.5px}
.about-title{left:264px;top:1112px;font-family:"Montserrat",sans-serif;font-weight:800;font-size:25px;line-height:30px;color:var(--navy)}
.about-title span{color:var(--cyan)}
.btn-about{left:264px;top:1179px;width:90px;background:var(--navy)}
.about-text{left:555px;top:1108px;width:385px;font-size:11.5px;line-height:17px;color:#8a9097}

/* services */
.services-band{left:0;top:1255px;width:1200px;height:836px;
  clip-path:polygon(0 107px,1200px 0,1200px 657px,0 836px);
  background:linear-gradient(180deg,#1c3460 10%,#2d5486 40%,#4c8fc2 75%,#6bb6de 100%)}
.services-eyebrow{left:0;width:1200px;top:1403px;text-align:center;font-size:10px;color:#c7d3e3}
.services-title{left:0;width:1200px;top:1410px;text-align:center;font-family:"Montserrat",sans-serif;font-size:38px;font-weight:700;color:var(--white)}
.svc-img{width:238px;height:177px}
.svc-meeting{left:243px;top:1497px;background:linear-gradient(135deg,#2b2a2a,#6a5d50 50%,#d8d6d2)}
.svc-passport{left:718px;top:1497px;background:linear-gradient(135deg,#d9b25f,#7a2f35 45%,#20263a)}
.svc-document{left:480px;top:1674px;background:linear-gradient(135deg,#f1f1f1,#cfcfcf 55%,#6f6a63)}
.svc-card{width:238px;height:177px;text-align:center;padding:0 16px}
.svc-card h3{font-family:"Montserrat",sans-serif;font-size:9.5px;font-weight:700;color:var(--white);margin-bottom:9px;white-space:nowrap}
.svc-card p{font-size:9px;line-height:12.5px;color:#c0d0e2;padding:0 8px}
.svc-business{left:480px;top:1497px;padding-top:52px}
.svc-corporate{left:243px;top:1674px;padding-top:52px}
.svc-migration{left:718px;top:1674px;padding-top:52px}
.btn-all{left:534px;top:1914px;width:132px;height:26px;border:1.5px solid var(--white)}

/* message */
.accent-box{left:220px;top:2150px;width:180px;height:320px;background:var(--blue-light)}
.photo-portrait{left:243px;top:2177px;width:357px;height:336px;
  background:linear-gradient(160deg,#2a3150,#4a3f5a 40%,#1a1c2a);box-shadow:0 6px 16px rgba(0,0,0,.3)}
.quote-mark{left:630px;top:2256px;font-family:"Montserrat",sans-serif;font-size:40px;font-weight:700;color:var(--grey-light);line-height:40px}
.quote-text{left:632px;top:2302px;width:322px;font-size:10.5px;line-height:16px;color:#5d636b}
.quote-name{left:632px;top:2398px;font-family:"Montserrat",sans-serif;font-size:19px;font-weight:700;color:var(--navy);line-height:22px}
.quote-role{left:632px;top:2424px;font-size:9px;color:var(--grey-light);letter-spacing:1px}

/* map */
.map{left:0;top:2545px;width:1200px;height:480px;
  clip-path:polygon(0 110px,1200px 0,1200px 420px,0 480px);
  background:linear-gradient(135deg,#383839,#2b2b2d 50%,#343436)}
.map-full{left:1176px;top:2547px;width:16px;height:16px;background:#e8e8e8}
.map-label{left:500px;top:2725px;width:204px;height:20px;background:var(--white);font-size:8.5px;color:#333;
  display:flex;align-items:center;padding-left:6px;white-space:nowrap}
.map-pin{left:589px;top:2752px}

/* contact */
.contact-title{left:250px;top:3090px;font-family:"Montserrat",sans-serif;font-size:36px;font-weight:700;color:var(--navy)}
.field{left:250px;width:343px;border:1px solid #cfd3d8;font-size:9.5px;color:#a8adb3;padding:5px 6px}
.f-name{top:3150px;height:25px}
.f-email{top:3183px;height:25px}
.f-msg{top:3215px;height:56px}
.btn-send{left:250px;top:3280px;width:343px;height:25px;background:var(--navy);color:var(--white);font-size:10px;
  display:flex;align-items:center;justify-content:center}
.col-head{font-family:"Montserrat",sans-serif;font-size:10.5px;font-weight:700;color:var(--navy)}
.col-text{font-size:9.5px;line-height:15px;color:var(--grey-light);white-space:nowrap}
.social{left:785px;top:3247px;display:flex;gap:11px}
.social span{width:25px;height:25px;background:var(--navy)}

/* footer */
.footer{left:0;top:3422px;width:1200px;height:150px;background:var(--navy)}
.footer-brand{left:318px;top:3472px;display:flex;flex-direction:column;align-items:center;gap:8px;color:var(--white);
  font-family:"Montserrat",sans-serif;font-weight:600;font-size:11px;letter-spacing:2px;text-align:center}
.footer-brand .brand-mark{width:22px;height:22px}
.f-head{font-family:"Montserrat",sans-serif;font-size:10px;font-weight:600;color:var(--white);white-space:nowrap}
.f-text{font-size:8.5px;line-height:12px;color:#aab7cb}
.news-input{left:730px;top:3487px;width:210px;height:21px;border-radius:11px;background:var(--white);overflow:hidden;
  font-size:8.5px;color:#a0a6ad;display:flex;align-items:center;padding-left:10px}
.news-send{position:absolute;right:0;top:0;width:46px;height:21px;background:#7b8595;color:var(--white);
  display:flex;align-items:center;justify-content:center}
.copyright{left:0;top:3572px;width:1200px;height:14px;background:#2a2f3a;color:#8d96a5;font-size:7.5px;
  display:flex;align-items:center;justify-content:center}
</style>
</head>
<body>

<!-- header and hero -->
<div class="abs hero" role="img" aria-label="City skyline across the harbour at dusk"></div>
<div class="abs hero-shade"></div>
<header class="abs navbar"></header>
<div class="abs brand"><span class="brand-mark"></span>HALVERN<br>LEGAL</div>
<nav>
  <span class="abs nav-link nav-home active">HOME</span>
  <span class="abs nav-link nav-about">ABOUT</span>
  <span class="abs nav-link nav-services">SERVICES</span>
  <span class="abs nav-link nav-contact">CONTACT</span>
</nav>
<div class="abs btn-start">GET STARTED NOW!</div>
<div class="abs hero-eyebrow">WELCOME TO</div>
<h1 class="abs hero-title">HALVERN LEGAL</h1>
<div class="abs hero-tag">IT'S ABOUT RESULTS.</div>
<p class="abs hero-text">Lorem ipsum dolor sit amet, consectetur adipiscing elit. Ut elit tellus, luctus nec ullamcorper mattis, pulvinar dapibus leo.</p>
<div class="abs btn-pill btn-learn">LEARN MORE</div>
<div class="abs btn-pill btn-contact">CONTACT US</div>

<!-- intro -->
<div class="abs eyebrow-s intro-eyebrow">Welcome To</div>
<h2 class="abs intro-title">Halvern<br>Legal</h2>
<div class="abs intro-rule"></div>
<div class="abs photo photo-handshake" role="img" aria-label="Black and white photo of a business handshake"></div>
<p class="abs small-text intro-text-a">I am text block. Click edit button to change this text. Lorem ipsum dolor sit amet, consectetur adipiscing elit.</p>
<p class="abs small-text intro-text-b">I am text block. Click edit button to change this text. Lorem ipsum dolor sit amet, consectetur adipiscing elit.</p>
<div class="abs photo photo-signing" role="img" aria-label="Black and white photo of a hand signing a document"></div>

<div class="abs about-eyebrow">Learn More About</div>
<h2 class="abs about-title">HALVERN LEGAL<br><span>WE GET RESULTS.</span></h2>
<div class="abs btn-pill btn-about">ABOUT US</div>
<p class="abs about-text">Lorem ipsum dolor sit amet conse ctetur adipisicing elit, sed do eiusmod tempor incididunt ut labore et dolore magna aliqua. Ut enim ad minim veniam, quis nostrud exercitation ullamco laboris nisi ut aliquip ex ea commodo consequat. Lorem ipsum dolor sit amet conse ctetur adipisicing elit, sed do eiusmod tempor incididunt.</p>

<!-- services -->
<section class="abs services-band"></section>
<div class="abs services-eyebrow">Learn More About</div>
<h2 class="abs services-title">Services</h2>
<div class="abs svc-img svc-meeting" role="img" aria-label="Photo of a business meeting at a desk"></div>
<div class="abs svc-card svc-business"><h3>Business Law and Dispute Resolution</h3><p>I am text block. Click edit button to change this text. Lorem ipsum dolor sit amet, consectetur adipiscing elit.</p></div>
<div class="abs svc-img svc-passport" role="img" aria-label="Photo of a passport and banknotes on a map"></div>
<div class="abs svc-card svc-corporate"><h3>Corporate Transactions and Regulation</h3><p>I am text block. Click edit button to change this text. Lorem ipsum dolor sit amet, consectetur adipiscing elit.</p></div>
<div class="abs svc-img svc-document" role="img" aria-label="Photo of a pen signing a contract"></div>
<div class="abs svc-card svc-migration"><h3>Migration Assistance</h3><p>I am text block. Click edit button to change this text. Lorem ipsum dolor sit amet, consectetur adipiscing elit.</p></div>
<div class="abs btn-pill btn-all">SEE ALL OUR SERVICES</div>

<!-- principal message -->
<div class="abs accent-box"></div>
<div class="abs photo-portrait" role="img" aria-label="Portrait of the principal lawyer in a suit with a night city behind"></div>
<div class="abs quote-mark">&ldquo;</div>
<p class="abs quote-text">I am text block. Click edit button to change this text. Lorem ipsum dolor sit amet, consectetur adipiscing elit. Ut elit tellus, luctus nec ullamcorper mattis, pulvinar dapibus leo. It is a long established fact that a reader will be distracted by the readable content of a page when looking at its layout.</p>
<div class="abs quote-name">Marcus Whitlow</div>
<div class="abs quote-role">HALVERN LEGAL CEO</div>

<!-- map -->
<div class="abs map" role="img" aria-label="Dark street map of the office location in Adelaide"></div>
<div class="abs map-full"></div>
<div class="abs map-label">48 Carrow Lane, Adelaide, South Australia</div>
<svg class="abs map-pin" width="18" height="26" viewBox="0 0 18 26"><path d="M9 0C4 0 0 4 0 9c0 7 9 17 9 17s9-10 9-17C18 4 14 0 9 0z" fill="#e84b3c"/><circle cx="9" cy="9" r="3.2" fill="#9b2418"/></svg>

<!-- contact -->
<h2 class="abs contact-title">Get in touch</h2>
<div class="abs field f-name">Name</div>
<div class="abs field f-email">Email</div>
<div class="abs field f-msg">Message</div>
<div class="abs btn-send">Send</div>

<div class="abs col-head" style="left:612px;top:3158px">LOCATION</div>
<p class="abs col-text" style="left:612px;top:3180px">48 Carrow Lane<br>Adelaide SA 5000</p>
<div class="abs col-head" style="left:612px;top:3226px">OUR HOURS</div>
<p class="abs col-text" style="left:612px;top:3248px">MON-FRI 9:00 – 17:00<br>SAT-SUN 10:00 – 14:00</p>

<div class="abs col-head" style="left:785px;top:3158px">CONTACT US</div>
<p class="abs col-text" style="left:785px;top:3180px">Phone: +61 8 8100 4250<br>Email: hello@halvernlegal.com</p>
<div class="abs col-head" style="left:785px;top:3226px">FOLLOW US</div>
<div class="abs social"><span></span><span></span><span></span><span></span></div>

<!-- footer -->
<footer class="abs footer"></footer>
<div class="abs footer-brand"><span class="brand-mark"></span>HALVERN<br>LEGAL</div>
<div class="abs f-head" style="left:430px;top:3460px">About Us</div>
<p class="abs f-text" style="left:430px;top:3478px;width:150px">Halvern Legal is a commercial law firm in Adelaide advising businesses on transactions, disputes and migration.</p>
<div class="abs f-head" style="left:605px;top:3460px">Useful Links</div>
<p class="abs f-text" style="left:605px;top:3480px">Home<br>About<br>Services<br>Contact</p>
<div class="abs f-head" style="left:730px;top:3460px">Subscribe To Our Newsletter</div>
<p class="abs f-text" style="left:730px;top:3472px">Get the latest legal news in your inbox.</p>
<div class="abs news-input">Email<span class="news-send">Send</span></div>
<div class="abs copyright">Copyright © 2018 Halvern Legal. All Rights Reserved.</div>

</body>
</html>
```